Verpackungen für kleine Imkerei
Zielgruppe
Wir sind eine kleine Imkerei aus dem Aargau (Schweiz) und stellen zusammen mit unseren glücklichen Bienen feinsten Honig her. Gerne möchten wir unseren visuelle Kommunikation nach aussen mit Hilfe eines neuen Etiketts verbessern.
Aufgabenstellung
Das Etikett muss rechteckig sein und wir auf einem runden Glas aufgeklebt. Die Maximalgrösse ist 210x45mm (beim 500g Glas) und entsprechend kleiner bei kleineren Einheiten. Wir möchten ein Grunddesign, welches adaptierbar ist auf die weiteren Sorten. (Waldhonig, Blütenhonig, cremiger Blütenhonig, Zürcher Stadthonig, Badener Stadthonig, Lenzburger Stadthonig). Barcode muss keinen eingefügt werden, nur die gesetzlichen Daten müssen auf dem Etiektt stehen. Weitere Wünsche und Anmerkungen befinden sich im pdf.
Sollten Dateien oder Bilder nachgereicht werden, bitte melden!

```html
<!DOCTYPE html>
<html lang="de">
<head>
<meta charset="utf-8">
<title>Sonnenwabe – Honigetikett Blütenhonig</title>
<link href="https://fonts.googleapis.com/css2?family=Roboto:wght@400;500;700&family=Roboto+Condensed:wght@700&display=swap" rel="stylesheet">
<style>
  :root{
    --bg:#ececec;
    --paper:#ffffff;
    --line:#c9c9c9;
    --ink:#2a2a2a;
    --ink-soft:#555555;
    --honey:#f6a81c;
    --honey-pale:#fde9c4;
    --wash-1:#f9c95a;
    --wash-2:#fde3a0;
    --wash-3:#fff6e2;
  }
  *{box-sizing:border-box;margin:0;padding:0}
  html,body{width:1200px;height:892px;overflow:hidden}
  body{background:var(--bg);font-family:"Roboto",sans-serif;color:var(--ink);position:relative}

  /* Lid tag */
  .lid-tag{position:absolute;left:460px;top:40px;width:280px;height:470px}
  .lid-tag svg{position:absolute;inset:0}
  .lid-tag__brand{position:absolute;left:0;right:0;top:118px;text-align:center;
    font-family:"Roboto",sans-serif;font-weight:500;font-size:40px;color:var(--ink)}
  .lid-tag__bee{position:absolute;width:34px;height:24px;border-radius:50%;
    background:radial-gradient(circle,var(--wash-1),var(--wash-2))}

  /* Label */
  .label{position:absolute;left:40px;top:556px;width:1120px;height:212px;
    background:var(--paper);border:1px solid var(--line);overflow:hidden}

  .label__legal{position:absolute;left:0;top:0;width:318px;height:100%;
    padding:12px 16px 0 18px;border-right:1px solid var(--line)}
  .legal__title{font-size:11px;font-weight:500;letter-spacing:2px;text-transform:uppercase;
    padding-bottom:6px;border-bottom:1px solid var(--ink-soft);width:150px}
  .legal__address{font-size:10px;line-height:13px;margin-top:6px;padding-bottom:6px;
    border-bottom:1px solid var(--ink-soft);width:150px}
  .legal__address strong{font-weight:700}
  .legal__storage{font-size:10px;line-height:13px;margin-top:6px;width:170px}
  .legal__codes{display:flex;gap:8px;margin-top:6px;font-size:9px;align-items:center}
  .legal__code{background:var(--honey-pale);padding:3px 6px}
  .legal__weight{position:absolute;left:18px;bottom:10px;font-size:22px;line-height:26px}

  .label__front{position:absolute;left:318px;top:0;width:620px;height:100%}
  .front__wash{position:absolute;left:60px;top:8px;width:520px;height:196px;
    background:radial-gradient(ellipse at 50% 50%,var(--wash-1) 0%,var(--wash-2) 45%,var(--wash-3) 75%,transparent 100%)}
  .front__tagline{position:absolute;left:0;right:0;top:16px;text-align:center;
    font-size:13px;line-height:16px;letter-spacing:.5px;text-transform:uppercase;color:var(--ink)}
  .front__brand{position:absolute;left:0;right:0;top:66px;text-align:center;
    font-family:"Roboto",sans-serif;font-weight:500;font-size:62px;color:var(--ink)}
  .front__variety{position:absolute;left:0;right:0;top:160px;text-align:center;
    font-family:"Roboto Condensed",sans-serif;font-weight:700;font-size:24px;letter-spacing:2px;color:var(--ink)}

  .label__info{position:absolute;right:0;top:0;width:168px;height:100%;
    background:var(--honey);color:var(--paper);padding:16px 14px;
    font-size:10.5px;line-height:14px;text-align:justify}
</style>
</head>
<body>

<section class="lid-tag" aria-label="Deckeletikett">
  <svg width="280" height="470" viewBox="0 0 280 470">
    <rect x="105" y="250" width="70" height="220" fill="#ffffff" stroke="#c9c9c9"/>
    <rect x="105.5" y="452" width="69" height="17.5" fill="#f6a81c"/>
    <circle cx="140" cy="140" r="138" fill="#ffffff" stroke="#c9c9c9"/>
    <rect x="106" y="262" width="68" height="20" fill="#ffffff"/>
  </svg>
  <div class="lid-tag__bee" style="left:70px;top:76px" role="img" aria-label="Gezeichnete Biene"></div>
  <div class="lid-tag__bee" style="left:176px;top:64px" role="img" aria-label="Gezeichnete Biene"></div>
  <div class="lid-tag__bee" style="left:80px;top:184px" role="img" aria-label="Gezeichnete Biene"></div>
  <div class="lid-tag__brand">Sonnenwabe</div>
</section>

<section class="label" aria-label="Rundetikett Blütenhonig">
  <div class="label__legal">
    <h2 class="legal__title">Schweizer Honig</h2>
    <p class="legal__address">
      Ursula &amp; Andreas Karrigo<br>
      Lindenmattweg 14<br>
      CH-5612 Rüttenau<br>
      <strong>www.sonnenwabe.ch</strong>
    </p>
    <p class="legal__storage">Den Honig gut verschlossen, trocken, dunkel, kühl bei max. 15° lagern. Mindestens haltbar bis:</p>
    <div class="legal__codes">
      <span class="legal__code">DD/MM/YY</span>
      <span>Lot-Nr:</span><span class="legal__code">LXXXXX</span>
    </div>
    <p class="legal__weight">500g</p>
  </div>

  <div class="label__front">
    <div class="front__wash" role="img" aria-label="Aquarellfläche in Honiggelb mit Blüten und Bienen"></div>
    <p class="front__tagline">Schweizer Honig<br>von glücklichen Bienen</p>
    <p class="front__brand">Sonnenwabe</p>
    <p class="front__variety">BLÜTENHONIG</p>
  </div>

  <div class="label__info">
    Unser Honig wird schonend geschleudert und kalt abgefüllt. Jedes Glas stammt aus eigenen Völkern im Aargau. Kristallisation ist ein natürliches Zeichen von Qualität und lässt sich im Wasserbad bei 40° lösen.
  </div>
</section>

</body>
</html>
```